Roofing Company Sales Rep Business Card

Business card for sales rep to canvass and hand out to property owners/managers for free roof inspections and roof replacements.

```html
<!DOCTYPE html>
<html lang="en">
<head>
<meta charset="utf-8">
<title>Ridgeline Roofing – Business Card</title>
<link rel="stylesheet" href="https://fonts.googleapis.com/css2?family=Montserrat:wght@400;500;700;800&display=swap">
<style>
  :root {
    --backdrop: #3b3b3d;
    --card-light: #ffffff;
    --card-dark: #1c1c1c;
    --brand-red: #e31e25;
    --ink: #2a2a2a;
    --paper-text: #ffffff;
  }
  * { margin: 0; padding: 0; box-sizing: border-box; }
  html, body {
    width: 1200px; height: 1059px; overflow: hidden;
    background: var(--backdrop);
    font-family: "Montserrat", sans-serif;
  }
  .card {
    position: absolute;
    border-radius: 19px;
    overflow: hidden;
  }
  .card--front {
    left: 256px; top: 100px; width: 688px; height: 391px;
    background: var(--card-light);
  }
  .card--back {
    left: 253px; top: 537px; width: 694px; height: 394px;
    background: var(--card-dark);
  }
  .wordmark {
    position: absolute;
    display: flex; align-items: center; gap: 8px;
    font-weight: 800; letter-spacing: 0.02em; white-space: nowrap;
    transform: translate(-50%, -50%);
  }
  .wordmark__square { background: var(--brand-red); flex: none; }
  .card--front .wordmark {
    left: 209px; top: 194px; font-size: 21px; color: var(--ink);
  }
  .card--front .wordmark__square { width: 14px; height: 14px; }
  .card--back .wordmark {
    left: 347px; top: 197px; font-size: 44px; color: var(--paper-text); gap: 14px;
  }
  .card--back .wordmark__square { width: 30px; height: 30px; }
  .divider {
    position: absolute; left: 345px; top: 126px;
    width: 2px; height: 139px; background: var(--brand-red);
  }
  .contact-block { position: absolute; left: 375px; top: 126px; }
  .contact-block__name {
    font-weight: 700; font-size: 26px; color: var(--brand-red);
    letter-spacing: 0.03em; line-height: 1.15;
  }
  .contact-block__role {
    font-weight: 500; font-size: 16px; color: var(--ink);
    letter-spacing: 0.06em; margin-top: 2px;
  }
  .contact-list { list-style: none; margin-top: 30px; }
  .contact-list li {
    display: flex; align-items: center; gap: 8px;
    font-size: 16px; color: var(--ink); height: 23.5px; letter-spacing: 0.02em;
  }
  .contact-list svg { width: 13px; height: 13px; fill: var(--brand-red); flex: none; }
  .address-band {
    position: absolute; left: 0; top: 315px; width: 100%; height: 28px;
    background: var(--brand-red); color: var(--paper-text);
    font-size: 15.5px; letter-spacing: 0.03em;
    display: flex; align-items: center; justify-content: center;
  }
</style>
</head>
<body>
  <section class="card card--front">
    <div class="wordmark"><span class="wordmark__square"></span>RIDGELINE ROOFING</div>
    <div class="divider"></div>
    <div class="contact-block">
      <h1 class="contact-block__name">DANA WHITFIELD</h1>
      <p class="contact-block__role">MANAGER</p>
      <ul class="contact-list">
        <li>
          <svg viewBox="0 0 24 24" aria-hidden="true"><path d="M6.6 10.8a15.1 15.1 0 0 0 6.6 6.6l2.2-2.2a1 1 0 0 1 1-.25 11.4 11.4 0 0 0 3.6.57 1 1 0 0 1 1 1V20a1 1 0 0 1-1 1A17 17 0 0 1 3 4a1 1 0 0 1 1-1h3.5a1 1 0 0 1 1 1c0 1.25.2 2.45.57 3.57a1 1 0 0 1-.25 1z"/></svg>
          (555) 014-2286
        </li>
        <li>
          <svg viewBox="0 0 24 24" aria-hidden="true"><path d="M2 5h20v14H2z" opacity="0"/><path d="M2 6.5 12 13l10-6.5V5H2zM2 8.8V19h20V8.8L12 15.3z"/></svg>
          hello@ridgelineroof.com
        </li>
        <li>
          <svg viewBox="0 0 24 24" aria-hidden="true"><path d="M12 2a10 10 0 1 0 0 20 10 10 0 0 0 0-20zm6.9 6h-3a15.6 15.6 0 0 0-1.4-3.6A8 8 0 0 1 18.9 8zM12 4c.8 1.2 1.5 2.5 1.9 4h-3.8c.4-1.5 1.1-2.8 1.9-4zM4.3 14a8.2 8.2 0 0 1 0-4h3.4a16 16 0 0 0 0 4zm.8 2h3a15.6 15.6 0 0 0 1.4 3.6A8 8 0 0 1 5.1 16zm3-8h-3a8 8 0 0 1 4.4-3.6A15.6 15.6 0 0 0 8.1 8zM12 20c-.8-1.2-1.5-2.5-1.9-4h3.8c-.4 1.5-1.1 2.8-1.9 4zm2.3-6H9.7a14.7 14.7 0 0 1 0-4h4.6a14.7 14.7 0 0 1 0 4zm.2 5.6a15.6 15.6 0 0 0 1.4-3.6h3a8 8 0 0 1-4.4 3.6zm1.8-5.6a16 16 0 0 0 0-4h3.4a8.2 8.2 0 0 1 0 4z"/></svg>
          www.ridgelineroof.com
        </li>
      </ul>
    </div>
    <div class="address-band">128 Cedar Lane, Suite 4, Fairview, OR 97024</div>
  </section>

  <section class="card card--back">
    <div class="wordmark"><span class="wordmark__square"></span>RIDGELINE ROOFING</div>
  </section>
</body>
</html>
```